Ashby Meadows Summer Swim Bag Tag Design

Hello!

We are looking to design a 2-sided bag tag for a children's summer swim team. Colors should be blue, white, pink. May also use a lighter blue or navy as an accent if needed. Attached are 2 files showing the look/feel of some of our other items. The bag tag would need to be in line with this same look.

Copy: Ashby Meadows Otters Swim 2026
#paddleon

The copy can be both on one side, or split between the 2 sides, either works. We are flexible! Needs to incorporate the 2026 logo into the design.

```html
<!DOCTYPE html>
<html lang="en">
<head>
<meta charset="utf-8">
<title>Ashby Meadows Otters Swim 2026 – Bag Tag</title>
<link rel="stylesheet" href="https://fonts.googleapis.com/css2?family=Anton&family=Archivo:wght@800&family=Kaushan+Script&family=Montserrat:wght@800&family=Roboto:ital@1&display=swap">
<style>
  :root {
    --royal: #1f4599;
    --pink: #f75a9e;
    --sky: #84bff0;
    --white: #ffffff;
    --ink: #111111;
    --mark: #333333;
  }
  html, body {
    margin: 0;
    width: 1200px;
    height: 625px;
    overflow: hidden;
    background: var(--white);
  }
  .sheet {
    position: relative;
    width: 1200px;
    height: 625px;
  }
  .spec-title {
    position: absolute;
    top: 34px;
    left: 0;
    width: 1200px;
    margin: 0;
    text-align: center;
    font-family: "Archivo", Arial, sans-serif;
    font-weight: 800;
    font-size: 30px;
    color: var(--ink);
    letter-spacing: 0.2px;
  }
  .spec-title .size { color: var(--pink); }
  .spec-note {
    position: absolute;
    top: 72px;
    left: 0;
    width: 1200px;
    margin: 0;
    text-align: center;
    font-family: "Roboto", Arial, sans-serif;
    font-style: italic;
    font-size: 22px;
    line-height: 29px;
    color: var(--ink);
  }
  .tag {
    position: absolute;
    top: 163px;
    overflow: visible;
  }
  .tag--front { left: 292px; width: 285px; height: 432px; }
  .tag--back  { left: 630px; width: 273px; height: 426px; }
  .crop { stroke: var(--mark); stroke-width: 0.8; }
  .t-club { font-family: "Montserrat", sans-serif; font-weight: 800; }
  .t-team { font-family: "Anton", sans-serif; }
  .t-year { font-family: "Montserrat", sans-serif; font-weight: 800; }
  .t-tagline { font-family: "Kaushan Script", cursive; }
</style>
</head>
<body>
<main class="sheet">
  <h1 class="spec-title">ATM CARD SIZE <span class="size">(53.98 x 85.60 mm)</span></h1>
  <p class="spec-note">(Scalable to any preferred size without losing quality,<br>as this is a vector file design.)</p>

  <!-- Front of bag tag -->
  <svg class="tag tag--front" viewBox="0 0 285 432" aria-label="Bag tag front">
    <g class="crop">
      <line x1="15" y1="-13" x2="15" y2="-1"/><line x1="270" y1="-13" x2="270" y2="-1"/>
      <line x1="-15" y1="13" x2="-1" y2="13"/><line x1="286" y1="13" x2="305" y2="13"/>
      <line x1="15" y1="433" x2="15" y2="445"/><line x1="270" y1="433" x2="270" y2="445"/>
      <line x1="-15" y1="418" x2="-1" y2="418"/><line x1="286" y1="418" x2="305" y2="418"/>
    </g>
    <rect class="tag-face" width="285" height="432" fill="var(--royal)"/>
    <text class="t-club" x="142.5" y="118" text-anchor="middle" font-size="21" fill="var(--white)" textLength="186" lengthAdjust="spacingAndGlyphs">ASHBY MEADOWS</text>
    <text class="t-team" x="34" y="192" font-size="76" fill="var(--pink)" textLength="217" lengthAdjust="spacingAndGlyphs">OTTERS</text>
    <g class="swim-banner">
      <line x1="34" y1="203" x2="76" y2="203" stroke="var(--pink)" stroke-width="2"/>
      <line x1="209" y1="203" x2="251" y2="203" stroke="var(--pink)" stroke-width="2"/>
      <polygon points="72,196 92,196 92,216 82,216 86,206 72,221" fill="var(--white)"/>
      <polygon points="213,196 193,196 193,216 203,216 199,206 213,221" fill="var(--white)"/>
      <rect x="88" y="191" width="109" height="24" fill="var(--white)"/>
      <text class="t-club" x="142.5" y="212" text-anchor="middle" font-size="20" fill="var(--royal)" letter-spacing="3">SWIM</text>
    </g>
    <text class="t-year" x="42" y="292" font-size="80" textLength="200" lengthAdjust="spacingAndGlyphs"><tspan fill="var(--white)">20</tspan><tspan fill="var(--pink)">26</tspan></text>
    <line x1="52" y1="306" x2="92" y2="306" stroke="var(--pink)" stroke-width="2"/>
    <line x1="192" y1="306" x2="234" y2="306" stroke="var(--pink)" stroke-width="2"/>
    <g role="img" aria-label="Water splash ornament">
      <rect x="118" y="296" width="50" height="24" rx="12" fill="var(--sky)"/>
    </g>
    <text class="t-tagline" x="142.5" y="352" text-anchor="middle" font-size="38" fill="var(--white)">#paddleon</text>
    <path d="M84 366 Q150 354 222 358" fill="none" stroke="var(--pink)" stroke-width="4" stroke-linecap="round"/>
  </svg>

  <!-- Back of bag tag -->
  <svg class="tag tag--back" viewBox="0 0 273 426" aria-label="Bag tag back">
    <g class="crop">
      <line x1="10" y1="-20" x2="10" y2="-1"/><line x1="263" y1="-20" x2="263" y2="-1"/>
      <line x1="-18" y1="13" x2="-1" y2="13"/><line x1="274" y1="13" x2="292" y2="13"/>
      <line x1="10" y1="427" x2="10" y2="440"/><line x1="263" y1="427" x2="263" y2="440"/>
      <line x1="-18" y1="418" x2="-1" y2="418"/><line x1="274" y1="418" x2="292" y2="418"/>
    </g>
    <rect class="tag-face" width="273" height="426" fill="var(--royal)"/>
    <text class="t-year" x="34" y="191" font-size="165" fill="var(--white)" textLength="86" lengthAdjust="spacingAndGlyphs">2</text>
    <g class="year-ring">
      <circle cx="180" cy="146" r="60" fill="var(--white)"/>
      <circle cx="180" cy="146" r="40" fill="var(--royal)"/>
      <text class="t-club" x="180" y="143" text-anchor="middle" font-size="11" fill="var(--white)">ASHBY</text>
      <text class="t-club" x="180" y="157" text-anchor="middle" font-size="11" fill="var(--white)">MEADOWS</text>
    </g>
    <text class="t-year" x="69" y="289" font-size="165" fill="var(--white)" textLength="87" lengthAdjust="spacingAndGlyphs">2</text>
    <text class="t-year" x="142" y="329" font-size="165" fill="var(--pink)" textLength="91" lengthAdjust="spacingAndGlyphs">6</text>
    <g class="waves">
      <path d="M0 345 C60 312 100 318 140 334 S220 360 273 330 L273 426 L0 426Z" fill="var(--white)"/>
      <path d="M0 362 C60 336 100 342 140 354 S220 374 273 350 L273 372 C220 388 180 378 140 370 S50 366 0 386Z" fill="var(--sky)"/>
      <path d="M0 396 C60 376 100 378 140 384 S220 392 273 378 L273 426 L0 426Z" fill="var(--pink)"/>
    </g>
  </svg>
</main>
</body>
</html>
```